Optometrist/Eye Care Clinic Business card with new logo attached

We are a small, independent eye care clinic in Canada. We have recently updated our logo (as attached), and would like a professional, modern and health care oriented business card to highlight our office details and our optometrist. We'd like to incorporate the blue colours as seen on our logo.

Target Market(s)

demographic: age 35-65 male/female equal

Industry/Entity Type

Health Care

Contact Information for Business Card

Name of clinic: "Amber Hollow Eye Care Optometry"

Font styles to use
Sans Serif

Colors
0355a3

Requirements
Must have
• our website: amberholloweyecare.net
• Dr Selma Okonkwo
• Optometrist
• 312-617 E Larkspur Ave
• Vancouver BC V7R 3P8
• P: 604-555-0193
• E: info@amberholloweyecare.net
Nice to have
• front side: logo/name of clinic as seen on logo attached and website
• backside: logo on the left side, and name/title/address/phone/email

```html
<!DOCTYPE html>
<html lang="en">
<head>
<meta charset="utf-8">
<title>Amber Hollow Eye Care Optometry – Business Card</title>
<link rel="stylesheet" href="https://fonts.googleapis.com/css2?family=Arimo:wght@400;700&display=swap">
<style>
  :root {
    --backdrop: #3b3b3b;
    --card-white: #f4f4f4;
    --navy: #003356;
    --sky: #2aa6dc;
    --body-grey: #505050;
    --white: #ffffff;
  }
  * { margin: 0; padding: 0; box-sizing: border-box; }
  html, body { width: 1200px; height: 960px; overflow: hidden; }
  body {
    background: var(--backdrop);
    font-family: "Arimo", Arial, sans-serif;
    position: relative;
  }
  .card {
    position: absolute;
    left: 310px;
    width: 600px;
    box-shadow: 0 3px 8px rgba(0,0,0,0.45);
  }
  .card--front { top: 113px; height: 343px; background: var(--card-white); }
  .card--back  { top: 512px; height: 342px; background: var(--navy); }

  /* front: clinic name, top right */
  .clinic-name {
    position: absolute; right: 44px; top: 96px;
    text-align: right;
    color: var(--navy);
    font-weight: 400;
    font-size: 16px;
    line-height: 22px;
    letter-spacing: 2.5px;
    text-transform: uppercase;
  }

  /* front: person & contact */
  .person { position: absolute; left: 45px; top: 157px; }
  .person__name { color: var(--navy); font-size: 22px; font-weight: 700; line-height: 26px; }
  .person__title { color: var(--sky); font-size: 15px; line-height: 18px; }
  .address {
    position: absolute; left: 45px; top: 210px;
    color: var(--body-grey); font-size: 14.5px; line-height: 19px;
  }
  .contact {
    position: absolute; left: 45px; top: 256px;
    list-style: none;
    color: var(--body-grey); font-size: 14.5px; line-height: 19px;
  }
  .contact li { display: flex; align-items: center; gap: 7px; }
  .contact svg { width: 14px; height: 14px; fill: var(--navy); flex: none; }

  /* back */
  .back-name {
    position: absolute; left: 0; right: 0; top: 132px;
    text-align: center;
    color: var(--white); font-size: 22px; line-height: 30px;
    letter-spacing: 4px; text-transform: uppercase; font-weight: 400;
  }
  .back-url {
    position: absolute; left: 0; right: 0; top: 291px;
    text-align: center; color: var(--white);
    font-size: 15px; letter-spacing: 2px;
  }
</style>
</head>
<body>
  <section class="card card--front">
    <p class="clinic-name">Amber Hollow<br>Eye Care<br>Optometry</p>

    <div class="person">
      <h1 class="person__name">Dr Selma Okonkwo</h1>
      <p class="person__title">Optometrist</p>
    </div>
    <p class="address">312-617 E Larkspur Ave<br>Vancouver BC V7R 3P8</p>
    <ul class="contact">
      <li>
        <svg viewBox="0 0 24 24" aria-hidden="true"><path d="M6.6 10.8a15.1 15.1 0 0 0 6.6 6.6l2.2-2.2c.3-.3.7-.4 1-.2 1.1.4 2.3.6 3.6.6.6 0 1 .4 1 1V20c0 .6-.4 1-1 1A17 17 0 0 1 3 4c0-.6.4-1 1-1h3.5c.6 0 1 .4 1 1 0 1.3.2 2.5.6 3.6.1.3 0 .7-.2 1z"/></svg>
        604-555-0193
      </li>
      <li>
        <svg viewBox="0 0 24 24" aria-hidden="true"><path d="M2 5h20v2l-10 6L2 7z"/><path d="M2 9l10 6 10-6v10H2z"/></svg>
        info@amberholloweyecare.net
      </li>
      <li>
        <svg viewBox="0 0 24 24" aria-hidden="true"><path d="M12 2a10 10 0 1 0 0 20 10 10 0 0 0 0-20zm-1 17.9A8 8 0 0 1 4.1 10L9 15v1c0 1.1.9 2 2 2zm6.9-2.5c-.3-.8-1-1.4-1.9-1.4h-1v-3c0-.6-.4-1-1-1H8v-2h2c.6 0 1-.4 1-1V7h2c1.1 0 2-.9 2-2v-.4a8 8 0 0 1 2.9 12.8z"/></svg>
        www.amberholloweyecare.net
      </li>
    </ul>
  </section>

  <section class="card card--back">
    <p class="back-name">Amber Hollow<br>Eye Care Optometry</p>
    <p class="back-url">www.amberholloweyecare.net</p>
  </section>
</body>
</html>
```